Corvath Holdings, LLC

We are a design build general contracting company.
We work with commercial accounts and private developers. We build retail spaces, restaurants and housing projects.
Im looking for a clean professional type of logo incorporating a roman flavor, think ionic columns and pedestals.
Two toned colorway.
I like unusual fonts and Im not afraid to do something bold with the logo.
Contact Information for Business Card
Marisol Brenkowitz
318-472-9051 corvathmb@mailvexo.com
Font styles to use
Decorative
Colors
Designer to choose colors to be used in the design.
Requirements
Should not have
- I don't like reds pinks.

```html
<!DOCTYPE html>
<html lang="en">
<head>
<meta charset="UTF-8">
<title>Corvath Holdings, LLC — Business Card</title>
<link rel="stylesheet" href="https://fonts.googleapis.com/css2?family=Mulish:wght@400;700&family=Roboto+Condensed:wght@700&family=Roboto:wght@400&display=swap">
<style>
  :root {
    --backdrop: #d4d4d4;
    --card-light: #f2f2f2;
    --card-dark: #1d1d1d;
    --ink: #2b2b2b;
    --ink-soft: #555555;
    --rule: #9a9a9a;
    --band-grey: #a3a3a3;
    --band-dark: #2c2c2c;
    --paper-white: #ffffff;
  }
  * { margin: 0; padding: 0; box-sizing: border-box; }
  html, body {
    width: 1200px; height: 960px; overflow: hidden;
    background: var(--backdrop);
  }
  .canvas { position: relative; width: 1200px; height: 960px; }

  .card { position: absolute; width: 600px; height: 343px; box-shadow: 0 2px 4px rgba(0,0,0,0.25); }
  .card--front { left: 302px; top: 129px; background: var(--card-light); overflow: hidden; }
  .card--back { left: 299px; top: 488px; background: var(--card-dark); }

  .front__company {
    position: absolute; right: 40px; top: 112px;
    font-family: "Mulish", sans-serif; font-weight: 700;
    font-size: 19px; color: var(--ink); letter-spacing: 0.2px;
  }
  .front__name {
    position: absolute; left: 40px; top: 205px;
    font-family: "Roboto Condensed", sans-serif; font-weight: 700;
    font-size: 23px; color: var(--ink); letter-spacing: 0.3px;
  }
  .front__rule {
    position: absolute; left: 40px; top: 241px; width: 520px; height: 1px;
    background: var(--rule);
  }
  .front__contacts {
    position: absolute; left: 41px; top: 254px; list-style: none;
    font-family: "Mulish", sans-serif; font-size: 14.5px; color: var(--ink-soft);
    line-height: 19px;
  }
  .front__contacts li { display: flex; align-items: center; gap: 7px; }
  .front__contacts svg { width: 13px; height: 13px; fill: var(--ink); flex: none; }

  .front__bands { position: absolute; left: 0; bottom: 0; width: 600px; height: 38px; }
  .front__web {
    position: absolute; right: 30px; bottom: 10px;
    font-family: "Roboto", sans-serif; font-size: 15px; letter-spacing: 2.6px;
    color: var(--paper-white);
  }

  .back__company {
    position: absolute; left: 0; right: 0; top: 140px; text-align: center;
    font-family: "Mulish", sans-serif; font-weight: 700;
    font-size: 36px; color: var(--paper-white);
  }
  .back__web {
    position: absolute; left: 0; right: 0; top: 288px; text-align: center;
    font-family: "Roboto", sans-serif; font-size: 15px; letter-spacing: 3px;
    color: var(--paper-white);
  }
</style>
</head>
<body>
<main class="canvas">
  <section class="card card--front" aria-label="Business card front">
    <p class="front__company">Corvath Holdings, LLC</p>
    <h1 class="front__name">MARISOL BRENKOWITZ</h1>
    <div class="front__rule"></div>
    <ul class="front__contacts">
      <li>
        <svg viewBox="0 0 24 24" aria-hidden="true"><path d="M6.6 10.8a15.1 15.1 0 0 0 6.6 6.6l2.2-2.2a1 1 0 0 1 1-.25 11.4 11.4 0 0 0 3.6.57 1 1 0 0 1 1 1V20a1 1 0 0 1-1 1A17 17 0 0 1 3 4a1 1 0 0 1 1-1h3.5a1 1 0 0 1 1 1c0 1.25.2 2.45.57 3.57a1 1 0 0 1-.25 1z"/></svg>
        318-472-9051
      </li>
      <li>
        <svg viewBox="0 0 24 24" aria-hidden="true"><path d="M2 5h20v14H2z M2 5l10 8 10-8" fill="none" stroke="#2b2b2b" stroke-width="0"/><path d="M2 5h20v2l-10 7L2 7z"/><path d="M2 9l10 7 10-7v10H2z"/></svg>
        corvathmb@mailvexo.com
      </li>
    </ul>
    <svg class="front__bands" viewBox="0 0 600 38" aria-hidden="true">
      <polygon points="0,24 356,24 347,37 0,37" fill="var(--band-grey)"/>
      <polygon points="381,0 600,0 600,38 352,38" fill="var(--band-dark)"/>
    </svg>
    <p class="front__web">www.corvathmb.com</p>
  </section>

  <section class="card card--back" aria-label="Business card back">
    <p class="back__company">Corvath Holdings, LLC</p>
    <p class="back__web">www.corvathmb.com</p>
  </section>
</main>
</body>
</html>
```